Copperfen Hollow Wine And Spirits

We need to design a website for our Liquor Store

Industry/Entity Type

Store

Number of Pages Required

4 page

Requirements
Must have
• Beer, Liquor, Wine & Cigar related theme.
• Mention our 8-locations addresses & maps info
Nice to have
• category for Beer, Liquor & Wine to setup database for item list to link our sql server database.

```html
<!DOCTYPE html>
<html lang="en">
<head>
<meta charset="utf-8">
<title>Copperfen Hollow Wine And Spirits</title>
<link rel="stylesheet" href="https://fonts.googleapis.com/css2?family=Roboto:wght@400;500;700&family=Great+Vibes&display=swap">
<style>
:root{
  --red:#c8202a;
  --red-dark:#a8161f;
  --ink:#2b2b2b;
  --muted:#8a8a8a;
  --line:#e2e2e2;
  --white:#ffffff;
  --black:#0b0b0b;
  --amber:#b86a12;
  --amber-dark:#3a1f08;
  --footer-bar:#1a1a1a;
  --sans:'Roboto', Arial, sans-serif;
  --script:'Great Vibes', cursive;
}
*{box-sizing:border-box;margin:0;padding:0}
html,body{width:1200px;height:3327px;overflow:hidden}
body{position:relative;font-family:var(--sans);color:var(--ink);background:var(--white)}
.abs{position:absolute}
.btn{position:absolute;display:flex;align-items:center;justify-content:center;background:var(--red);color:var(--white);font:500 13px/1 var(--sans);text-transform:uppercase;border-radius:6px;letter-spacing:.3px}
.script-title{position:absolute;font:400 40px/1 var(--script);color:var(--ink);text-align:center}
.script-title::after{content:"";display:block;width:70px;height:1px;background:#bbb;margin:10px auto 0}

/* hero */
.hero{position:absolute;left:0;top:0;width:1200px;height:517px;background:radial-gradient(ellipse at 50% 40%,#7a4b1c 0%,#3d2410 55%,#1d1108 100%)}
.hero-beer{position:absolute;left:0;top:0;width:460px;height:517px;background:linear-gradient(160deg,#5a3614 0%,#d9951f 55%,#f1c24a 75%,#6b3e12 100%)}
.hero-whisky{position:absolute;left:800px;top:120px;width:400px;height:397px;background:linear-gradient(200deg,#2a1608 0%,#a8620f 50%,#e7a23a 70%,#3b220b 100%)}
.hero-circle{position:absolute;left:388px;top:30px;width:424px;height:424px;border-radius:50%;background:rgba(255,255,255,.86)}
.brand{position:absolute;left:472px;top:58px;width:256px;height:118px;display:flex;align-items:center;justify-content:center;gap:10px}
.brand-mark{width:18px;height:18px;background:var(--red)}
.brand-name{font:700 22px/1.15 var(--sans);color:#1e2a55;text-align:left;text-transform:uppercase}
.hero-title{position:absolute;left:388px;top:205px;width:424px;text-align:center;font:400 39px/1 var(--sans);color:var(--red);letter-spacing:.5px}
.hero-text{position:absolute;left:460px;top:262px;width:280px;text-align:center;font:500 15px/1.42 var(--sans);color:#222}
.menu-toggle{position:absolute;left:1048px;top:20px;width:44px;height:44px}

/* about */
.about-title{left:268px;top:602px;width:240px}
.about-text{position:absolute;left:135px;top:675px;width:505px;text-align:center;font:400 12.5px/1.65 var(--sans);color:var(--muted)}
.about-bottles{position:absolute;left:820px;top:548px;width:380px;height:357px;background:linear-gradient(180deg,#ffffff 0%,#f3d8a0 20%,#b8681b 55%,#7a3d0e 80%,#dfe6ea 100%)}

/* nav band */
.cat-nav{position:absolute;left:0;top:905px;width:1200px;height:66px;background:var(--red);display:flex;justify-content:center;align-items:center;padding-right:60px}
.cat-nav a{color:var(--white);text-decoration:none;font:500 15px/1 var(--sans);padding:0 42px;border-right:1px solid rgba(255,255,255,.55);height:38px;display:flex;align-items:center}
.cat-nav a:last-child{border-right:none}

/* gallery */
.gallery-tile{position:absolute;top:971px;height:304px}
.tile-barrels{left:0;width:402px;background:linear-gradient(135deg,#3e240e 0%,#a66312 45%,#e4a73a 65%,#4a2a0e 100%)}
.tile-bar{left:402px;width:403px;background:linear-gradient(180deg,#5a1016 0%,#8a1a22 100%)}
.tile-bar-overlay{position:absolute;left:402px;top:971px;width:403px;height:304px;background:rgba(200,32,42,.72);display:flex;flex-direction:column;align-items:center;justify-content:center;gap:14px;color:var(--white)}
.tile-bar-overlay h3{font:400 31px/1 var(--sans)}
.tile-taps{left:805px;width:395px;background:linear-gradient(180deg,#2a1607 0%,#c17a18 45%,#f0b447 60%,#3a2009 100%)}

/* category */
.category-title{left:480px;top:1332px;width:240px}
.price-col{position:absolute;top:1425px;width:322px}
.price-col h3{text-align:center;font:400 20px/1 var(--sans);color:var(--ink);margin-bottom:20px}
.price-row{display:flex;align-items:baseline;font:400 12.5px/21px var(--sans);color:#555}
.price-row .leader{flex:1;border-bottom:1px dotted #999;margin:0 3px;transform:translateY(-4px)}
.price-col .btn{position:absolute;left:100px;top:189px;width:130px;height:28px}

/* blog */
.blog{position:absolute;left:0;top:1708px;width:1200px;height:521px;background:linear-gradient(180deg,#1a0f07 0%,#4a2a12 55%,#1b1009 100%)}
.blog-photo{position:absolute;left:244px;top:1752px;width:339px;height:433px;background:linear-gradient(180deg,#2a1709 0%,#6a3d14 40%,#e0a232 70%,#3a200b 100%);border:2px solid #d9d9d9}
.blog-panel{position:absolute;left:583px;top:1752px;width:373px;height:433px;background:var(--white)}
.blog-title{left:583px;top:1775px;width:373px}
.blog-item{position:absolute;left:583px;width:373px;height:84px}
.blog-item.active{width:382px;background:var(--red)}
.blog-date{position:absolute;left:20px;top:14px;width:56px;height:56px;background:var(--red);color:var(--white);text-align:center}
.blog-item.active .blog-date{background:var(--white);color:var(--red)}
.blog-date b{display:block;font:400 28px/1 var(--sans);padding-top:6px;padding-right:10px}
.blog-date small{display:block;font:400 10px/1 var(--sans);padding-right:10px}
.blog-date i{position:absolute;right:3px;top:3px;width:8px;font:700 9px/12px var(--sans);font-style:normal;color:var(--red);background:var(--white);height:50px}
.blog-item.active .blog-date i{background:var(--red);color:var(--white)}
.blog-item h4{position:absolute;left:102px;top:14px;font:500 14px/1 var(--sans);color:var(--red)}
.blog-item p{position:absolute;left:102px;top:33px;width:250px;font:400 12px/1.6 var(--sans);color:var(--muted)}
.blog-item.active h4,.blog-item.active p{color:var(--white)}

/* services */
.services-title{left:480px;top:2292px;width:240px}
.service{position:absolute;top:2388px;width:250px;text-align:center}
.service-icon{width:72px;height:72px;margin:0 auto 26px;display:block}
.service h4{font:400 15px/1 var(--sans);color:var(--ink);margin-bottom:9px}
.service p{font:400 12px/1.55 var(--sans);color:var(--muted);width:220px;margin:0 auto}

/* locations */
.locations{position:absolute;left:0;top:2628px;width:1200px;height:471px;background:linear-gradient(180deg,#2a1a0e 0%,#5a3618 50%,#24160b 100%)}
.map{position:absolute;left:98px;top:2673px;width:443px;height:383px;background:linear-gradient(135deg,#eceae4 0%,#dcdad2 50%,#e8e6df 100%);border:2px solid #d0d0d0}
.loc-panel{position:absolute;left:541px;top:2673px;width:499px;height:383px;background:var(--white)}
.loc-title{left:541px;top:2688px;width:499px}
.loc-title::after{width:60px;margin-top:8px}
.loc-card{position:absolute;left:599px;width:417px;height:84px;border:1px solid #cfcfcf;border-radius:6px;background:var(--white);box-shadow:0 2px 3px rgba(0,0,0,.12)}
.loc-card.active{background:var(--red);border-color:var(--red);color:var(--white)}
.loc-card.active::before{content:"";position:absolute;left:-13px;top:24px;border:12px solid transparent;border-right-color:var(--red);border-left:0}
.loc-line{position:absolute;display:flex;gap:8px;font:400 11.5px/1.35 var(--sans);color:#333}
.loc-card.active .loc-line{color:var(--white)}
.loc-line svg{flex:none;margin-top:1px}
.scroll-track{position:absolute;left:1050px;top:2740px;width:8px;height:300px;background:#eee;border-radius:4px}
.scroll-thumb{position:absolute;left:1050px;top:2740px;width:8px;height:40px;background:var(--red);border-radius:4px}

/* footer */
.footer{position:absolute;left:0;top:3099px;width:1200px;height:195px;background:var(--black);color:var(--white)}
.footer-col{position:absolute;top:20px}
.footer-col h5{font:500 14px/1 var(--sans);margin-bottom:16px}
.footer-col p,.footer-col li{font:400 12.5px/1.6 var(--sans);list-style:none}
.footer-col.links li{line-height:24px}
.copyright{position:absolute;left:0;top:3294px;width:1200px;height:33px;background:var(--footer-bar);color:#ddd;font:400 12px/33px var(--sans);text-align:center}
</style>
</head>
<body>

<!-- Hero -->
<header class="hero" role="img" aria-label="Photo of beer mugs, a barrel tap and whisky glasses on a bar"></header>
<div class="hero-beer" role="img" aria-label="Wooden barrel with tap and two foaming beer mugs"></div>
<div class="hero-whisky" role="img" aria-label="Two glasses of whisky on ice"></div>
<div class="hero-circle"></div>
<div class="brand">
  <span class="brand-mark"></span>
  <span class="brand-name">Copperfen Hollow<br>Wine &amp; Spirits</span>
</div>
<h1 class="hero-title">LOREM IPSUM IS</h1>
<p class="hero-text">Lorem Ipsum is simply dummy text of the printing and typesetting industry. Lorem Ipsum has been the industry's standard dummy text ever since the.</p>
<a class="btn" style="left:531px;top:384px;width:136px;height:35px;border-radius:8px">Read More</a>
<svg class="menu-toggle" viewBox="0 0 44 44" aria-label="Menu">
  <circle cx="22" cy="22" r="19" fill="none" stroke="#fff" stroke-width="2.5"/>
  <path d="M13 15h18M13 22h18M13 29h18" stroke="#fff" stroke-width="3" stroke-linecap="round"/>
</svg>

<!-- About -->
<h2 class="script-title about-title">About Us</h2>
<p class="about-text">Lorem Ipsum is simply dummy text of the printing and typesetting industry. Lorem Ipsum has been the industry's standard dummy text ever since the 1500s, when an unknown printer took a galley of type and scrambled it to make a type specimen book. It has survived not only five centuries.</p>
<a class="btn" style="left:320px;top:787px;width:132px;height:30px">Read More</a>
<div class="about-bottles" role="img" aria-label="Two beer bottles resting in crushed ice"></div>

<!-- Category nav -->
<nav class="cat-nav"><a>Beer</a><a>Liquor</a><a>Wine</a></nav>

<!-- Gallery -->
<div class="gallery-tile tile-barrels" role="img" aria-label="Barrels, bottles and beer glasses on a table"></div>
<div class="gallery-tile tile-bar" role="img" aria-label="Interior of a bar with stools"></div>
<div class="tile-bar-overlay">
  <h3>Lorem Ipsum is simply</h3>
  <svg width="28" height="28" viewBox="0 0 28 28" aria-label="Search"><circle cx="11.5" cy="11.5" r="8" fill="none" stroke="#fff" stroke-width="3"/><path d="M17.5 17.5l7 7" stroke="#fff" stroke-width="3.5" stroke-linecap="round"/></svg>
</div>
<div class="gallery-tile tile-taps" role="img" aria-label="Row of beer glasses under bar taps"></div>

<!-- Category price lists -->
<h2 class="script-title category-title">Category</h2>

<section class="price-col" style="left:100px">
  <h3>Wine</h3>
  <div class="price-row"><span>Ipsum is simply dummy</span><span class="leader"></span><span>$ 5235.00</span></div>
  <div class="price-row"><span>Orem Ipsum is simply dummy</span><span class="leader"></span><span>$ 8235.00</span></div>
  <div class="price-row"><span>Rem Ipsum is dummy</span><span class="leader"></span><span>$ 9235.00</span></div>
  <div class="price-row"><span>psum is simply dummy</span><span class="leader"></span><span>$ 2235.00</span></div>
  <div class="price-row"><span>Orem Ipsum is simply dummy</span><span class="leader"></span><span>$ 4235.00</span></div>
  <div class="price-row"><span>Rem Ipsum is dummy</span><span class="leader"></span><span>$ 3235.00</span></div>
  <a class="btn">View More</a>
</section>
<section class="price-col" style="left:441px">
  <h3>Beer</h3>
  <div class="price-row"><span>Ipsum is simply dummy</span><span class="leader"></span><span>$ &nbsp;&nbsp;235.00</span></div>
  <div class="price-row"><span>Orem Ipsum is simply dummy</span><span class="leader"></span><span>$ 1235.00</span></div>
  <div class="price-row"><span>Rem Ipsum is dummy</span><span class="leader"></span><span>$ 1035.00</span></div>
  <div class="price-row"><span>psum is simply dummy</span><span class="leader"></span><span>$ 4235.00</span></div>
  <div class="price-row"><span>Orem Ipsum is simply dummy</span><span class="leader"></span><span>$ 8235.00</span></div>
  <div class="price-row"><span>Rem Ipsum is dummy</span><span class="leader"></span><span>$ 9235.00</span></div>
  <a class="btn">View More</a>
</section>
<section class="price-col" style="left:782px">
  <h3>Liquore</h3>
  <div class="price-row"><span>Ipsum is simply dummy</span><span class="leader"></span><span>$ 2235.00</span></div>
  <div class="price-row"><span>Orem Ipsum is simply dummy</span><span class="leader"></span><span>$ 9235.00</span></div>
  <div class="price-row"><span>Rem Ipsum is dummy</span><span class="leader"></span><span>$ 1235.00</span></div>
  <div class="price-row"><span>psum is simply dummy</span><span class="leader"></span><span>$ 5235.00</span></div>
  <div class="price-row"><span>Orem Ipsum is simply dummy</span><span class="leader"></span><span>$ 6235.00</span></div>
  <div class="price-row"><span>Rem Ipsum is dummy</span><span class="leader"></span><span>$ 4235.00</span></div>
  <a class="btn">View More</a>
</section>

<!-- Blog -->
<section class="blog" role="img" aria-label="Blurred bar counter with warm lights"></section>
<div class="blog-photo" role="img" aria-label="Glass of beer beside a copper bucket on a bar"></div>
<div class="blog-panel"></div>
<h2 class="script-title blog-title">Our Blog</h2>

<article class="blog-item active" style="top:1845px">
  <div class="blog-date"><b>22</b><small>January</small><i>2<br>0<br>1<br>7</i></div>
  <h4>Lorem Ipsum is simply</h4>
  <p>Ipsum is simply dummy text of the printing and typesetting industry.</p>
</article>
<article class="blog-item" style="top:1960px">
  <div class="blog-date"><b>22</b><small>January</small><i>2<br>0<br>1<br>7</i></div>
  <h4>Lorem Ipsum is simply</h4>
  <p>Ipsum is simply dummy text of the printing and typesetting industry.</p>
</article>
<article class="blog-item" style="top:2071px">
  <div class="blog-date"><b>22</b><small>January</small><i>2<br>0<br>1<br>7</i></div>
  <h4>Lorem Ipsum is simply</h4>
  <p>Ipsum is simply dummy text of the printing and typesetting industry.</p>
</article>

<!-- Services -->
<h2 class="script-title services-title">Our Services</h2>
<div class="service" style="left:132px">
  <svg class="service-icon" viewBox="0 0 72 72" role="img" aria-label="Service icon"><circle cx="36" cy="36" r="34" fill="none" stroke="#c8202a" stroke-width="2"/><circle cx="36" cy="36" r="28" fill="#f6d7d9"/><rect x="22" y="34" width="28" height="12" rx="3" fill="#c8202a"/></svg>
  <h4>Is simply dummy</h4>
  <p>Lorem Ipsum is simply dummy text of the printing and typesetting industry.</p>
</div>
<div class="service" style="left:474px">
  <svg class="service-icon" viewBox="0 0 72 72" role="img" aria-label="Service icon"><circle cx="36" cy="36" r="34" fill="none" stroke="#c8202a" stroke-width="2"/><circle cx="36" cy="36" r="28" fill="#f6d7d9"/><rect x="25" y="40" width="22" height="14" rx="3" fill="#c8202a"/><rect x="29" y="20" width="14" height="16" rx="7" fill="#c8202a"/></svg>
  <h4>Is simply dummy</h4>
  <p>Lorem Ipsum is simply dummy text of the printing and typesetting industry.</p>
</div>
<div class="service" style="left:815px">
  <svg class="service-icon" viewBox="0 0 72 72" role="img" aria-label="Service icon"><circle cx="36" cy="36" r="34" fill="none" stroke="#c8202a" stroke-width="2"/><circle cx="36" cy="36" r="28" fill="#f6d7d9"/><rect x="22" y="24" width="28" height="24" rx="2" fill="none" stroke="#c8202a" stroke-width="3"/><path d="M22 32h28" stroke="#c8202a" stroke-width="3"/></svg>
  <h4>Is simply dummy</h4>
  <p>Lorem Ipsum is simply dummy text of the printing and typesetting industry.</p>
</div>

<!-- Locations -->
<section class="locations" role="img" aria-label="Blurred bar interior background"></section>
<div class="map" role="img" aria-label="Street map showing the store locations"></div>
<div class="loc-panel"></div>
<h2 class="script-title loc-title">Our Locations</h2>

<div class="loc-card active" style="top:2744px">
  <div class="loc-line" style="left:24px;top:8px"><svg width="11" height="11" viewBox="0 0 12 12"><path d="M2 1l3 0 1 3-1.5 1a7 7 0 0 0 3 3L9 6.5l3 1v3c-6 1-11-4-10-10z" fill="currentColor"/></svg>000 - 0000 - 00000</div>
  <div class="loc-line" style="left:226px;top:8px"><svg width="12" height="10" viewBox="0 0 12 10"><rect width="12" height="10" rx="1" fill="currentColor"/><path d="M0 1l6 4 6-4" stroke="#c8202a" fill="none"/></svg>hello@copperfenhollow.com</div>
  <div class="loc-line" style="left:24px;top:30px;width:190px"><svg width="11" height="11" viewBox="0 0 12 12"><path d="M6 0l6 5h-2v7H2V5H0z" fill="currentColor"/></svg><span>Lorem Ipsum is simply<br>and typesetting industry.<br>the industry's standard</span></div>
  <div class="loc-line" style="left:226px;top:30px"><svg width="11" height="11" viewBox="0 0 12 12"><circle cx="6" cy="6" r="5.5" fill="currentColor"/><path d="M6 3v3.5h2.5" stroke="#c8202a" fill="none"/></svg><span>Monday - Saturday<br>10.00 am - 10.00 pm<br>Sunday - Closed</span></div>
</div>
<div class="loc-card" style="top:2848px">
  <div class="loc-line" style="left:24px;top:8px"><svg width="11" height="11" viewBox="0 0 12 12"><path d="M2 1l3 0 1 3-1.5 1a7 7 0 0 0 3 3L9 6.5l3 1v3c-6 1-11-4-10-10z" fill="#333"/></svg>000 - 0000 - 00000</div>
  <div class="loc-line" style="left:226px;top:8px"><svg width="12" height="10" viewBox="0 0 12 10"><rect width="12" height="10" rx="1" fill="#333"/><path d="M0 1l6 4 6-4" stroke="#fff" fill="none"/></svg>hello@copperfenhollow.com</div>
  <div class="loc-line" style="left:24px;top:30px"><svg width="11" height="11" viewBox="0 0 12 12"><path d="M6 0l6 5h-2v7H2V5H0z" fill="#333"/></svg><span>Lorem Ipsum is simply<br>and typesetting industry.<br>the industry's standard</span></div>
  <div class="loc-line" style="left:226px;top:30px"><svg width="11" height="11" viewBox="0 0 12 12"><circle cx="6" cy="6" r="5.5" fill="#333"/><path d="M6 3v3.5h2.5" stroke="#fff" fill="none"/></svg><span>Monday - Saturday<br>10.00 am - 10.00 pm<br>Sunday - Closed</span></div>
</div>
<div class="loc-card" style="top:2952px">
  <div class="loc-line" style="left:24px;top:8px"><svg width="11" height="11" viewBox="0 0 12 12"><path d="M2 1l3 0 1 3-1.5 1a7 7 0 0 0 3 3L9 6.5l3 1v3c-6 1-11-4-10-10z" fill="#333"/></svg>000 - 0000 - 00000</div>
  <div class="loc-line" style="left:226px;top:8px"><svg width="12" height="10" viewBox="0 0 12 10"><rect width="12" height="10" rx="1" fill="#333"/><path d="M0 1l6 4 6-4" stroke="#fff" fill="none"/></svg>hello@copperfenhollow.com</div>
  <div class="loc-line" style="left:24px;top:30px"><svg width="11" height="11" viewBox="0 0 12 12"><path d="M6 0l6 5h-2v7H2V5H0z" fill="#333"/></svg><span>Lorem Ipsum is simply<br>and typesetting industry.<br>the industry's standard</span></div>
  <div class="loc-line" style="left:226px;top:30px"><svg width="11" height="11" viewBox="0 0 12 12"><circle cx="6" cy="6" r="5.5" fill="#333"/><path d="M6 3v3.5h2.5" stroke="#fff" fill="none"/></svg><span>Monday - Saturday<br>10.00 am - 10.00 pm<br>Sunday - Closed</span></div>
</div>
<div class="scroll-track"></div>
<div class="scroll-thumb"></div>

<!-- Footer -->
<footer class="footer">
  <div class="footer-col" style="left:100px;width:290px">
    <h5>About Us</h5>
    <p>Lorem Ipsum is simply dummy text of the printing and typesetting industry. Lorem Ipsum has been the industry's standard dummy text ever since the 1500s, when an unknown printer took a galley of type and scrambled i make a type specimen book.</p>
  </div>
  <div class="footer-col" style="left:501px;width:210px">
    <h5>Recent News</h5>
    <p>Ipsum is simply dummy text of the printing and typesetting<br>12/08/2017</p>
    <p style="margin-top:12px">Ipsum is simply dummy text of the printing and typesetting<br>12/08/2017</p>
  </div>
  <div class="footer-col links" style="left:843px">
    <h5>Quick Links</h5>
    <ul><li>Home</li><li>About Us</li><li>Category</li><li>Our Blog</li><li>Contact Us</li></ul>
  </div>
  <div class="footer-col links" style="left:1038px">
    <h5>Category</h5>
    <ul><li>Wine</li><li>Beer</li><li>Liquore</li></ul>
  </div>
</footer>
<div class="copyright">CopperfenHollow.com © 2015-2017 All rights reserved. Privacy policy</div>

</body>
</html>
```